Non profit organization looking for new flyers as "leaflets"

Hi, we are looking for new flyers in form "leaflets in German :-)" i've attached our old flyer, we have new logo and thats why we need new and better design smt ... "New: I've so attached the text Regarding the old cards with minor changes "

Industry/Entity Type

Non Profit

Font styles to use
Sans Serif

```html
<!DOCTYPE html>
<html lang="de">
<head>
<meta charset="utf-8">
<title>Lumera – Ambulante Erziehungshilfe Faltblatt</title>
<link href="https://fonts.googleapis.com/css2?family=Lato:wght@400;700;900&family=Oswald:wght@400;500&display=swap" rel="stylesheet">
<style>
  :root{
    --green:#7cb82f;
    --green-dark:#5e9b24;
    --lime:#c4d52b;
    --ink:#2b3239;
    --ink-soft:#3a434b;
    --paper:#f6f6f6;
    --paper-shade:#e9eaea;
    --text:#222;
    --accent-text:#b3c92a;
  }
  html,body{margin:0;padding:0;width:1200px;height:1200px;overflow:hidden;background:#fff;}
  .canvas{position:relative;width:1200px;height:1200px;}
  .leaflet{
    position:absolute;left:30px;top:195px;width:1020px;height:724px;
    transform:scale(1.1176);transform-origin:0 0;
    font-family:'Lato',sans-serif;
  }
  .panel{position:absolute;top:0;width:340px;height:697px;overflow:hidden;}
  .panel--left{left:0;background:linear-gradient(180deg,#fff 0%,var(--paper) 60%,var(--paper-shade) 100%);}
  .panel--middle{left:340px;background:var(--ink);}
  .panel--right{left:680px;background:linear-gradient(180deg,#fafafa 0%,var(--paper) 60%,var(--paper-shade) 100%);}
  .shapes{position:absolute;left:0;top:0;width:1020px;height:697px;}
  .footer-band{position:absolute;left:0;top:697px;width:1020px;height:27px;background:linear-gradient(90deg,var(--green) 0%,#8cc63f 50%,var(--green) 100%);}

  .photo-phone{position:absolute;left:30px;top:30px;width:262px;height:200px;
    background:radial-gradient(ellipse at 55% 50%,#6b6e72 0%,#a9acaf 45%,#fff 75%);}
  .body-copy{position:absolute;left:43px;width:270px;font-size:14.2px;line-height:17.5px;color:var(--text);text-align:justify;margin:0;}
  .body-copy--one{top:377px;}
  .body-copy--two{top:482px;}

  .brand{position:absolute;display:flex;align-items:center;gap:12px;}
  .brand__dot{width:26px;height:26px;border-radius:50%;background:var(--green);}
  .brand__name{font-family:'Lato',sans-serif;font-weight:900;font-size:42px;letter-spacing:.5px;color:var(--ink-soft);line-height:1;}
  .brand--left{left:56px;top:604px;}
  .brand--right{left:40px;top:72px;}
  .brand--middle{left:82px;top:438px;gap:10px;}
  .brand--middle .brand__name{font-size:32px;color:#fff;}
  .brand--middle .brand__dot{width:20px;height:20px;background:#fff;}

  .middle-top{position:absolute;left:0;top:0;width:340px;height:380px;
    background:linear-gradient(160deg,var(--lime) 0%,#9fc830 40%,var(--green) 100%);}
  .map-area{position:absolute;left:52px;top:48px;width:236px;height:212px;background:#666;border-radius:18px;}
  .contact{position:absolute;left:0;top:512px;width:340px;text-align:center;color:#fff;font-size:15.5px;line-height:19.5px;margin:0;}
  .tagline{position:absolute;left:0;top:657px;width:340px;text-align:center;font-size:13px;color:var(--accent-text);margin:0;letter-spacing:.1px;}
  .tagline--right{color:var(--green-dark);}

  .photo-family{position:absolute;left:0;top:0;width:340px;height:697px;}
  .title{position:absolute;left:0;width:340px;text-align:center;font-family:'Oswald',sans-serif;font-weight:500;margin:0;line-height:1;}
  .title--main{top:558px;font-size:44px;color:var(--green);letter-spacing:-.5px;}
  .title--sub{top:607px;font-size:38px;color:var(--ink);font-weight:400;letter-spacing:-.8px;}
</style>
</head>
<body>
<div class="canvas">
  <div class="leaflet">

    <section class="panel panel--left">
      <div class="photo-phone" role="img" aria-label="Foto eines Bürotelefons"></div>
      <p class="body-copy body-copy--one">Lorem ipsum dolor sit amet, consectetur adipiscing elit. Mauris quis sagittis turpis. Maecenas varius ex elit, nec accumsan leo sagittis sit amet. Nulla tincidunt, lacus eu faucibus consequat, felis leo efficitur velit,</p>
      <p class="body-copy body-copy--two">Lorem ipsum dolor sit amet, consectetur adipiscing elit. Mauris quis sagittis turpis. Maecenas varius ex elit, nec accumsan leo sagittis sit amet. Nulla tincidunt, lacus eu faucibus consequat, felis leo efficitur velit,</p>
      <div class="brand brand--left"><span class="brand__dot"></span><span class="brand__name">lumera</span></div>
    </section>

    <section class="panel panel--middle">
      <div class="middle-top"></div>
      <div class="map-area" role="img" aria-label="Karte der Region mit Pfeilen"></div>
      <div class="brand brand--middle"><span class="brand__dot"></span><span class="brand__name">lumera</span></div>
      <p class="contact">Lumera Sundorf<br>Lindenweg 12<br>59821 Sundorf<br>Mail: kontakt@lumera-lw.de<br>Tel. 0 12 34 – 567 89 10<br>Fax 0 12 34 – 567 89 11</p>
      <p class="tagline">LUMERA.LERNWERK E.V</p>
    </section>

    <section class="panel panel--right">
      <svg class="photo-family" viewBox="0 0 340 697" role="img" aria-label="Foto einer streitenden Familie mit Kind">
        <defs>
          <linearGradient id="familyTone" x1="0" y1="0" x2="1" y2="1">
            <stop offset="0" stop-color="#cfd6dc"/>
            <stop offset=".5" stop-color="#a89a8e"/>
            <stop offset="1" stop-color="#7f8890"/>
          </linearGradient>
        </defs>
        <polygon points="0,245 180,182 340,242 340,424 0,517" fill="url(#familyTone)"/>
      </svg>
      <div class="brand brand--right"><span class="brand__dot"></span><span class="brand__name">lumera</span></div>
      <h1 class="title title--main">AMBULKLANTE</h1>
      <h2 class="title title--sub">ERZIEHUNGSHILFE</h2>
      <p class="tagline tagline--right">LUMERA.LERNWERK E.V</p>
    </section>

    <svg class="shapes" viewBox="0 0 1020 697" aria-hidden="true">
      <!-- left panel diagonals -->
      <polygon points="0,232 340,360 340,372 0,244" fill="var(--ink)"/>
      <polygon points="22,242 190,254 336,362" fill="var(--green)"/>
      <!-- middle panel divider -->
      <polygon points="340,362 680,236 680,252 340,376" fill="#fff"/>
      <polygon points="346,380 532,358 680,256 680,262 340,384" fill="var(--green)"/>
      <!-- right panel chevron top -->
      <polygon points="680,230 860,168 1020,226 1020,238 860,182 680,245" fill="var(--ink)"/>
      <polygon points="680,245 860,182 1020,238 1020,244 860,190 680,251" fill="var(--green)"/>
      <!-- right panel bottom lines -->
      <polygon points="680,511 1020,418 1020,425 680,518" fill="var(--green)"/>
      <polygon points="680,518 1020,425 1020,432 680,525" fill="var(--ink)"/>
      <polygon points="690,532 880,512 1020,436 1020,444" fill="var(--green)"/>
    </svg>

    <div class="footer-band"></div>
  </div>
</div>
</body>
</html>
```